2012 Calendar Design

This calendar will be a Ironpulse themed calendar (http://games.ironpulse.example/) for more about ironpulse. It is fitness related and should graphically relate to the ironpulse style as seen on the website. Darker, a bit grungy is good...

Calendar to 8.5 x 11 designed in adobe indesign and completely editable, allowing for updates and changes to the images, calendar, dates. Detail specs are as follows;

Width = 8.25 in / Height = 10.75
Margins: Top = 0.25 in / Bottom = 0.25 in / Inside = 0.25 in / Outside = 0.25 in
Bleeds: Top = 0.125 in / Bottom = 0.125 in / Inside = 0 in / Outside = 0.25 in

See here for example of final layout;

http://www.printvane.example/browse/issue/731562

I will provide image files for each page.

Target Market(s)

Ironpulse Athelets, Gym Owners, Sports and Nutrition

Industry/Entity Type

Fitness

Requirements
Must have
• Designed in Adobe Indesign and fully editable

```html
<!DOCTYPE html>
<html lang="en">
<head>
<meta charset="utf-8">
<title>Ironpulse 2012 Calendar – January</title>
<link href="https://fonts.googleapis.com/css2?family=Oswald:wght@600;700&family=Open+Sans:wght@400;700&family=Crimson+Text:wght@400&display=swap" rel="stylesheet">
<style>
  :root {
    --page-bg: #ffffff;
    --paper: #c39a5e;
    --paper-light: #d9b983;
    --paper-dark: #9d7440;
    --frame: #5a3f22;
    --rule: #8a2f17;
    --year-top: #d8521c;
    --year-bottom: #7a1f10;
    --label-red: #8e2a22;
    --day-head: #8c3a16;
    --date-ink: #1f140a;
    --white: #ffffff;
    --photo-light: #a88a5c;
    --photo-dark: #3a2a18;
  }
  * { box-sizing: border-box; margin: 0; padding: 0; }
  html, body {
    width: 932px; height: 1200px; overflow: hidden;
    background: var(--page-bg);
  }
  .calendar-page {
    position: absolute; left: 23px; top: 23px;
    width: 906px; height: 1168px;
    background:
      radial-gradient(ellipse at 55% 75%, var(--paper-light) 0%, var(--paper) 55%, var(--paper-dark) 100%);
    border: 1px solid var(--frame);
    overflow: hidden;
  }
  .top-band {
    position: absolute; left: 0; top: 0; width: 100%; height: 45px;
    background: linear-gradient(180deg, #b58a50, #d1ae74);
  }
  .hero-photo {
    position: absolute; left: 0; top: 45px; width: 906px; height: 602px;
    background:
      radial-gradient(ellipse at 50% 45%, var(--photo-light) 0%, #7a5e38 55%, var(--photo-dark) 100%);
  }
  .divider {
    position: absolute; left: 33px; top: 693px; width: 850px; height: 2px;
    background: var(--rule);
  }
  .brand-block { position: absolute; left: 53px; top: 730px; width: 210px; text-align: center; }
  .year {
    font-family: "Oswald", sans-serif; font-weight: 700;
    font-size: 74px; line-height: 1; letter-spacing: 2px;
    background: linear-gradient(180deg, var(--year-top), var(--year-bottom));
    -webkit-background-clip: text; background-clip: text; color: transparent;
  }
  .year-label {
    font-family: "Open Sans", sans-serif; font-weight: 700;
    font-size: 28px; line-height: 1; color: var(--label-red);
    margin-top: 2px; letter-spacing: 0.5px;
  }
  .intro {
    position: absolute; left: 49px; top: 878px; width: 218px;
    font-family: "Open Sans", sans-serif; font-size: 12.4px; line-height: 15.4px;
    color: var(--white); text-align: justify;
  }
  .column-rule {
    position: absolute; left: 277px; top: 719px; width: 2px; height: 375px;
    background: var(--rule);
  }
  .month-name {
    position: absolute; left: 292px; top: 993px;
    transform: rotate(-90deg); transform-origin: 0 0;
    font-family: "Oswald", sans-serif; font-weight: 700;
    font-size: 60px; line-height: 1; color: var(--white);
    letter-spacing: 0.5px;
  }
  .month-grid { position: absolute; left: 358px; top: 740px; }
  .day-head, .date {
    position: absolute; width: 60px; text-align: center; transform: translateX(-30px);
  }
  .day-head {
    font-family: "Open Sans", sans-serif; font-weight: 700;
    font-size: 22px; color: var(--day-head);
  }
  .date {
    font-family: "Crimson Text", serif; font-size: 38px; line-height: 1;
    color: var(--date-ink);
  }
</style>
</head>
<body>
<main class="calendar-page">
  <div class="top-band"></div>
  <div class="hero-photo" role="img" aria-label="Sepia photograph of a group of athletes running into the surf, seen from behind"></div>
  <div class="divider"></div>

  <div class="brand-block">
    <div class="year">2012</div>
    <div class="year-label">CALENDAR</div>
  </div>

  <p class="intro">Ironpulse begins with a belief in fitness. The aim of Ironpulse is to forge a broad, general, and inclusive fitness. We have sought to build a program that will best prepare trainees for any physical contingency—not only for the unknown, but for the unknowable. After looking at all sport and physical tasks collectively, we asked what physical skills and adaptations would most universally lend themselves to</p>

  <div class="column-rule"></div>
  <div class="month-name">January</div>

  <div class="month-grid">
    <span class="day-head" style="left:38px;top:0">S</span>
    <span class="day-head" style="left:114px;top:0">M</span>
    <span class="day-head" style="left:190px;top:0">T</span>
    <span class="day-head" style="left:269px;top:0">W</span>
    <span class="day-head" style="left:347px;top:0">T</span>
    <span class="day-head" style="left:426px;top:0">F</span>
    <span class="day-head" style="left:502px;top:0">S</span>

    <span class="date" style="left:502px;top:116px">1</span>

    <span class="date" style="left:38px;top:172px">2</span>
    <span class="date" style="left:114px;top:172px">3</span>
    <span class="date" style="left:190px;top:172px">4</span>
    <span class="date" style="left:269px;top:172px">5</span>
    <span class="date" style="left:347px;top:172px">6</span>
    <span class="date" style="left:426px;top:172px">7</span>
    <span class="date" style="left:502px;top:172px">8</span>

    <span class="date" style="left:38px;top:222px">9</span>
    <span class="date" style="left:114px;top:222px">10</span>
    <span class="date" style="left:190px;top:222px">11</span>
    <span class="date" style="left:269px;top:222px">12</span>
    <span class="date" style="left:347px;top:222px">13</span>
    <span class="date" style="left:426px;top:222px">14</span>
    <span class="date" style="left:502px;top:222px">15</span>

    <span class="date" style="left:38px;top:271px">16</span>
    <span class="date" style="left:114px;top:271px">17</span>
    <span class="date" style="left:190px;top:271px">18</span>
    <span class="date" style="left:269px;top:271px">19</span>
    <span class="date" style="left:347px;top:271px">20</span>
    <span class="date" style="left:426px;top:271px">21</span>
    <span class="date" style="left:502px;top:271px">22</span>

    <span class="date" style="left:38px;top:318px">23</span>
    <span class="date" style="left:114px;top:318px">24</span>
    <span class="date" style="left:190px;top:318px">25</span>
    <span class="date" style="left:269px;top:318px">26</span>
    <span class="date" style="left:347px;top:318px">27</span>
    <span class="date" style="left:426px;top:318px">28</span>
    <span class="date" style="left:502px;top:318px">29</span>

    <span class="date" style="left:38px;top:365px">30</span>
    <span class="date" style="left:114px;top:365px">31</span>
  </div>
</main>
</body>
</html>
```